MLD Illustration Web Design

Create illustration web design company for Mandirasa Luhur Digital (MLD). I more prefer design with illustration concept. Detail for requirement please see attach file. I'm also attach MLD logo. This logo had 2 type, 2D design and 3D design. You can chose one of them, or used both.
For the winner or had good design would be possible to private project to completeness this website
Attach file requirement is guidance for design, but any changes are welcome
Updates
Sorry, I forgot about contact. Please add menu contact. You can put this menu besides login menu or part of menu level #1, or put on some where to adjust your design. Menu contact will give pop up window to email MLD Company and Company Information (Address, Telephone, etc)
Target Market(s)
Company (Business To Business)
Industry/Entity Type
It Company
Look and feel
Each slider illustrates characteristics of the customer's brand and the style your logo design should communicate.

```html
<!DOCTYPE html>
<html lang="en">
<head>
<meta charset="utf-8">
<title>MLD — Ideas Beyond Immagination</title>
<link href="https://fonts.googleapis.com/css2?family=Barlow+Condensed:wght@500;600;700&family=Arimo:wght@400;700&display=swap" rel="stylesheet">
<style>
:root{
  --sky:#3cc3d3;
  --sky-light:#bfeef3;
  --white:#ffffff;
  --paper:#f6f7f7;
  --green:#7aaa1c;
  --green-light:#b9d630;
  --green-dark:#4f8a12;
  --blue:#1f8fbb;
  --blue-dark:#0f6a93;
  --ink:#222222;
  --tag:#1d1d1d;
  --line:#555555;
  --hill:#8cc83a;
  --hill-dark:#5f9f24;
}
*{margin:0;padding:0;box-sizing:border-box}
html,body{width:1200px;height:727px;overflow:hidden}
body{font-family:"Arimo",Arial,sans-serif;background:var(--white);color:var(--ink)}
.page{position:relative;width:1200px;height:727px;overflow:hidden;background:var(--white)}

.sky{position:absolute;left:0;top:0;width:1200px;height:465px;
  background:linear-gradient(to bottom,var(--white) 0%,var(--white) 14%,var(--sky-light) 22%,var(--sky) 33%,#6fd3de 62%,#e9f8fa 88%,var(--white) 100%)}
.cloud-band{position:absolute;left:0;top:60px;width:1200px;height:45px;
  background:linear-gradient(to bottom,var(--white) 0%,rgba(255,255,255,.85) 45%,rgba(255,255,255,0) 100%)}

.brand{position:absolute;left:426px;top:10px;display:flex;align-items:center;gap:10px}
.brand-mark{width:72px;height:72px;border-radius:50%;background:var(--blue-dark)}
.brand-name{font-family:"Barlow Condensed",sans-serif;font-weight:700;color:var(--green);line-height:1}
.brand-name .short{display:block;font-size:64px;letter-spacing:4px}
.brand-name .long{display:block;font-size:12.5px;letter-spacing:1.6px;margin-top:0}

.rail{position:absolute;left:122px;top:0;width:2px;height:535px;background:var(--line)}

.utility{position:absolute;left:40px;top:50px;list-style:none}
.utility li{width:92px;height:24px;margin-bottom:4px;background:var(--tag);color:var(--white);
  font-family:"Barlow Condensed",sans-serif;font-weight:600;font-size:14px;display:flex;align-items:center;gap:5px;padding-left:16px;
  transform:skewY(-5deg);box-shadow:0 2px 3px rgba(0,0,0,.35)}
.utility .dot{width:10px;height:10px;border-radius:50%;background:var(--blue)}
.utility li.contact .dot{background:var(--green-light)}

.nav{position:absolute;left:114px;top:120px;list-style:none}
.nav li{position:relative;width:128px;height:44px;margin-bottom:1px;
  background:linear-gradient(to bottom,var(--green-dark),var(--green-light));
  color:var(--white);font-family:"Barlow Condensed",sans-serif;font-weight:600;font-size:21px;
  display:flex;align-items:center;justify-content:center;gap:10px;transform:skewY(5deg);
  text-shadow:0 1px 2px rgba(0,0,0,.4)}
.nav li.home{width:141px;height:52px;background:linear-gradient(to bottom,var(--blue),var(--blue-dark));margin-bottom:2px}
.nav .caret{width:14px;height:14px;border-radius:50%;background:var(--white);position:relative}
.nav .caret::after{content:"";position:absolute;left:4px;top:3px;width:4px;height:4px;border-right:1.5px solid var(--green);border-bottom:1.5px solid var(--green);transform:rotate(45deg)}

.headline{position:absolute;left:298px;top:138px;font-family:"Barlow Condensed",sans-serif;font-weight:600;font-size:58px;letter-spacing:.5px;white-space:nowrap;text-shadow:0 2px 3px rgba(0,0,0,.18)}
.headline .w{color:var(--white)}
.headline .g{color:var(--green)}
.headline .b{color:var(--blue-dark)}

.hero-art{position:absolute;left:392px;top:206px;width:562px;height:262px;border-radius:40% 40% 30% 30%;
  background:radial-gradient(ellipse at 50% 40%,#7fc53a 0%,#5ea63a 35%,#7fa9b8 70%,rgba(180,210,220,0) 100%)}

.content{position:absolute;left:0;top:463px;width:1200px;height:170px;background:linear-gradient(to bottom,#e3e6e6 0,var(--paper) 4px,var(--white) 100%)}
.welcome{position:absolute;left:201px;top:494px;font-family:"Barlow Condensed",sans-serif;font-weight:600;font-size:32px;line-height:36px}
.welcome .g{display:block;color:var(--green)}
.welcome .b{display:block;color:var(--blue)}
.intro{position:absolute;left:544px;top:493px;width:470px;font-size:12px;line-height:19.3px;color:var(--ink)}
.more{position:absolute;left:543px;top:583px;width:85px;height:23px;background:linear-gradient(to bottom,var(--blue),var(--blue-dark));
  color:var(--white);font-family:"Barlow Condensed",sans-serif;font-weight:600;font-size:15px;display:flex;align-items:center;justify-content:center}

.landscape{position:absolute;left:0;top:615px;width:1200px;height:112px;
  background:linear-gradient(to bottom,rgba(140,200,58,0) 0%,var(--hill-dark) 12%,var(--hill) 45%,#9fd148 100%)}

.footer{position:absolute;left:0;top:686px;width:1200px;height:22px;font-size:12px}
.copyright{position:absolute;left:201px;top:4px;color:var(--ink)}
.share{position:absolute;top:1px;display:flex;align-items:center;gap:4px}
.share .btn{height:17px;padding:0 6px;background:#f2f2f2;border:1px solid #bcbcbc;border-radius:2px;font-size:11px;font-weight:700;color:#333;display:flex;align-items:center}
.share .count{height:17px;padding:0 5px;background:var(--white);border:1px solid #bcbcbc;font-size:10px;display:flex;align-items:center}
.social{position:absolute;left:850px;top:0;display:flex;gap:3px;list-style:none}
.social li{width:22px;height:22px;border-radius:50%;background:var(--white);border:1px solid #cfd8c4}
</style>
</head>
<body>
<main class="page">
  <div class="sky"></div>
  <div class="cloud-band" role="img" aria-label="Band of soft white clouds along the top edge"></div>

  <header class="brand">
    <span class="brand-mark"></span>
    <span class="brand-name"><span class="short">MLD</span><span class="long">MANDIRASA LUHUR DIGITAL</span></span>
  </header>

  <div class="rail"></div>

  <ul class="utility">
    <li class="login"><span class="dot"></span>LOGIN</li>
    <li class="contact"><span class="dot"></span>CONTACT</li>
  </ul>

  <ul class="nav">
    <li class="home">HOME</li>
    <li>SERVICES <span class="caret"></span></li>
    <li>PRODUCTS <span class="caret"></span></li>
    <li>CLIENTS</li>
    <li>COMPANY <span class="caret"></span></li>
    <li>BLOG</li>
  </ul>

  <h1 class="headline"><span class="w">IDEAS</span> <span class="g">BEYOND</span> <span class="b">IMMAGINATION</span></h1>

  <div class="content"></div>
  <div class="hero-art" role="img" aria-label="Floating green island with a lake, waterfall, city towers, a printing press, a tablet and an airship"></div>

  <h2 class="welcome"><span class="g">WELCOME TO</span><span class="b">MANDIRASA LUHUR DIGITAL</span></h2>
  <p class="intro">Lorem ipsum dolor sit amet, consectetuer adipiscing elit, sed diam nonummy nibh euismod tincidunt ut laoreet dolore magna aliquam erat volutpat. Ut wisi enim ad minim veniam, quis nostrud exerci tation ullamcorper suscipit lobortis nisl ut aliquip ex ea commodo consequat.</p>
  <a class="more">READ MORE</a>

  <div class="landscape" role="img" aria-label="Rolling green hills with small trees and a windmill"></div>

  <footer class="footer">
    <span class="copyright">Copyright © 2013 | MLD. All rights reserved</span>
    <div class="share" style="left:495px"><span class="btn">Share</span><span class="count">2</span></div>
    <div class="share" style="left:590px"><span class="btn">Like</span><span class="count">0</span></div>
    <div class="share" style="left:697px"><span class="btn">Plus</span><span class="count">2</span></div>
    <div class="share" style="left:775px"><span class="btn">Save</span></div>
    <ul class="social"><li></li><li></li><li></li><li></li></ul>
  </footer>
</main>
</body>
</html>
```